Bref créative
Business Cards & Letterhead for a business that owns franchises
HARTWELL HOLDINGS GROUP
Professional
Gregory T. Pennock, Sr.
President & Co-Owner
3852 Fernhollow Bend, SE
Atlanta, GA
Gregory@HartHoldingsGroup.example
www.hartholdingsgroup.example
Our Logo? Be Creative!!
HARTWELL HOLDINGS GROUP LOGO

```html
<!DOCTYPE html>
<html lang="en">
<head>
<meta charset="utf-8">
<title>Hartwell Holdings Group – Stationery Set</title>
<link rel="stylesheet" href="https://fonts.googleapis.com/css2?family=Lato:wght@400;700&display=swap">
<style>
  :root {
    --paper: #ffffff;
    --stage: #ffffff;
    --frame: #e3e3e3;
    --brand-red: #c8242b;
    --brand-grey: #8a8d91;
    --ink: #55585c;
    --shadow: rgba(0, 0, 0, 0.28);
  }
  * { box-sizing: border-box; margin: 0; padding: 0; }
  html, body { width: 1200px; height: 681px; overflow: hidden; background: var(--stage); }
  .stage {
    position: relative; width: 1200px; height: 681px;
    border: 1px solid var(--frame);
    font-family: "Lato", "Helvetica Neue", Arial, sans-serif;
    color: var(--ink);
  }
  .sheet {
    position: absolute; background: var(--paper);
    box-shadow: 2px 3px 7px var(--shadow);
    overflow: hidden;
  }

  /* Brand mark: plain circle + wordmark */
  .brand { position: absolute; display: flex; flex-direction: column; align-items: center; }
  .brand-circle { border: 2px solid var(--brand-grey); border-radius: 50%; }
  .brand-name {
    font-family: "Lato", "Helvetica Neue", Arial, sans-serif;
    font-weight: 700; color: var(--brand-red);
    letter-spacing: 0.06em; white-space: nowrap; line-height: 1.1; text-align: center;
  }

  /* Rules */
  .rule { position: absolute; height: 3px; }
  .rule-red { background: var(--brand-red); }
  .rule-grey { background: var(--brand-grey); }

  .contact { position: absolute; font-size: 7px; line-height: 1.45; color: var(--ink); white-space: nowrap; }
  .contact-center { text-align: center; transform: translateX(-50%); }

  /* Envelope front */
  .envelope-front { left: 43px; top: 101px; width: 528px; height: 206px; }
  .envelope-front .brand { left: 14px; top: 12px; }
  .envelope-front .brand-circle { width: 32px; height: 32px; }
  .envelope-front .brand-name { font-size: 8px; width: 70px; white-space: normal; margin-top: 3px; }

  /* Envelope back */
  .envelope-back { left: 43px; top: 336px; width: 528px; height: 211px; }
  .envelope-flap { position: absolute; left: 0; top: 0; }
  .envelope-back .brand { left: 249px; top: 14px; }
  .envelope-back .brand-circle { width: 30px; height: 30px; }

  /* Letterhead */
  .letterhead { left: 600px; top: 48px; width: 396px; height: 600px; }
  .letterhead .brand { left: 0; right: 0; top: 22px; }
  .letterhead .brand-circle { width: 42px; height: 42px; }
  .letterhead .brand-name { font-size: 13px; margin-top: 5px; }
  .letterhead .contact { font-size: 7.5px; }

  /* Business cards */
  .card-front { left: 972px; top: 173px; width: 156px; height: 110px; }
  .card-front .brand { left: 0; right: 0; top: 6px; }
  .card-front .brand-circle { width: 16px; height: 16px; border-width: 1.5px; }
  .card-front .brand-name { font-size: 5.5px; margin-top: 2px; }
  .card-person { position: absolute; right: 10px; top: 36px; text-align: right; line-height: 1.3; }
  .card-person-name { font-size: 6.5px; font-weight: 700; color: var(--ink); }
  .card-person-title { font-size: 5.5px; color: var(--brand-grey); }
  .card-front .rule { height: 2px; }
  .card-front .contact { font-size: 4.6px; line-height: 1.5; left: 78px; top: 64px; }

  .card-back { left: 972px; top: 307px; width: 156px; height: 106px; }
  .card-back .brand { left: 62px; top: 37px; }
  .card-back .brand-circle { width: 32px; height: 32px; }
</style>
</head>
<body>
<main class="stage">

  <!-- Envelope, front -->
  <section class="sheet envelope-front" aria-label="Envelope front">
    <div class="brand">
      <span class="brand-circle"></span>
      <span class="brand-name">HARTWELL HOLDINGS GROUP</span>
    </div>
    <span class="rule rule-red" style="left:0; top:80px; width:368px;"></span>
    <span class="rule rule-grey" style="left:372px; top:80px; width:148px;"></span>
    <p class="contact contact-center" style="left:318px; top:160px;">
      3852 Fernhollow Bend, SE &nbsp;|&nbsp; Atlanta, GA 30316<br>
      Cell: 404.555.0148 &nbsp;|&nbsp; Phone: 404.555.0193 &nbsp;|&nbsp; Fax: 404.555.0172<br>
      Gregory@HartHoldingsGroup.example &nbsp;|&nbsp; www.hartholdingsgroup.example
    </p>
  </section>

  <!-- Envelope, back -->
  <section class="sheet envelope-back" aria-label="Envelope back">
    <svg class="envelope-flap" width="528" height="211" viewBox="0 0 528 211" aria-hidden="true">
      <path d="M0 0 Q6 40 30 46 L498 46 Q522 40 528 0" fill="none" stroke="#9a9a9a" stroke-width="1"/>
    </svg>
    <div class="brand">
      <span class="brand-circle"></span>
    </div>
  </section>

  <!-- Letterhead -->
  <section class="sheet letterhead" aria-label="Letterhead">
    <div class="brand">
      <span class="brand-circle"></span>
      <span class="brand-name">HARTWELL HOLDINGS GROUP</span>
    </div>
    <span class="rule rule-grey" style="left:12px; top:148px; width:70px;"></span>
    <span class="rule rule-red" style="left:84px; top:148px; width:252px;"></span>
    <span class="rule rule-grey" style="left:340px; top:148px; width:50px;"></span>
    <p class="contact contact-center" style="left:198px; top:548px;">
      3852 Fernhollow Bend, SE &nbsp;|&nbsp; Atlanta, GA 30316<br>
      Cell: 404.555.0148 &nbsp;|&nbsp; Phone: 404.555.0193 &nbsp;|&nbsp; Fax: 404.555.0172<br>
      Gregory@HartHoldingsGroup.example &nbsp;|&nbsp; www.hartholdingsgroup.example
    </p>
  </section>

  <!-- Business card, front -->
  <section class="sheet card-front" aria-label="Business card front">
    <div class="brand">
      <span class="brand-circle"></span>
      <span class="brand-name">HARTWELL HOLDINGS GROUP</span>
    </div>
    <div class="card-person">
      <p class="card-person-name">Gregory T. Pennock, Sr.</p>
      <p class="card-person-title">President &amp; Co-Owner</p>
    </div>
    <span class="rule rule-red" style="left:0; top:56px; width:108px;"></span>
    <span class="rule rule-grey" style="left:110px; top:56px; width:46px;"></span>
    <p class="contact contact-center">
      3852 Fernhollow Bend, SE | Atlanta, GA 30316<br>
      Cell: 404.555.0148 | Phone: 404.555.0193<br>
      Fax: 404.555.0172<br>
      Gregory@HartHoldingsGroup.example<br>
      www.hartholdingsgroup.example
    </p>
  </section>

  <!-- Business card, back -->
  <section class="sheet card-back" aria-label="Business card back">
    <div class="brand">
      <span class="brand-circle"></span>
    </div>
  </section>

</main>
</body>
</html>
```